Label Quorvel Beer Can for Exhibition promo not consumer sale

label for exhibtion promotional craft beer. I publish international trade techology magazines and after 13 years are unveiling a redesign for the magazines- new logo, new paper etc. The beer is for drinking and I am sure will get a bit of social promo within the trade.

Target Market(s)

Exhibtion Attendees, clients, readers

Colors

Requirements
Must have
• Ultimately, it is 205mm wide by 87mm high. The guides in the file show the correct split for an aesthetically pleasing design that will get all the important info/branding on the front, and the legal stuff like the barcode and allergens on the back. Once done ,we will also likely need the source files too so that the correct barcode and ingredients can be dropped in
Nice to have
• We prefer a lorquist can style (document 1)

```html
<!DOCTYPE html>
<html lang="en">
<head>
<meta charset="utf-8">
<title>Quorvel Promo Can Label</title>
<link rel="stylesheet" href="https://fonts.googleapis.com/css2?family=DM+Serif+Display&family=Playball&display=swap">
<style>
  :root {
    --page: #ffffff;
    --sky-pale: #eefafd;
    --wave-top-1: #7fcfe3;
    --wave-top-3: #bde6f0;
    --wave-blue: #0a7fd6;
    --wave-navy: #0b3a82;
    --wave-cyan: #14d0dc;
    --badge-dark: #312c4c;
    --badge-light: #4a437c;
    --brand-ink: #eefafd;
    --ribbon-dark: #4e9a12;
    --ribbon-light: #9ee44a;
    --promo-ink: #4b3a8c;
  }
  * { margin: 0; padding: 0; box-sizing: border-box; }
  html, body {
    width: 1200px;
    height: 1200px;
    overflow: hidden;
    background: var(--page);
  }
  .can-label {
    position: absolute;
    left: 50px;
    top: 366px;
    width: 1100px;
    height: 466px;
    overflow: hidden;
    box-shadow: 0 10px 40px rgba(0, 0, 0, 0.25);
  }
  .can-label__waves {
    position: absolute;
    inset: 0;
    background: linear-gradient(180deg,
      var(--wave-top-1) 0px,
      var(--wave-top-3) 80px,
      var(--sky-pale) 120px,
      var(--sky-pale) 250px,
      var(--wave-blue) 310px,
      var(--wave-navy) 370px,
      var(--wave-cyan) 430px,
      var(--wave-cyan) 466px);
  }
  .badge {
    position: absolute;
    left: 431px;
    top: 58px;
    width: 280px;
    height: 280px;
    border-radius: 50%;
    background: linear-gradient(90deg, var(--badge-dark), var(--badge-light));
    box-shadow: 0 6px 18px rgba(40, 40, 90, 0.25);
  }
  .brand-name {
    position: absolute;
    left: 431px;
    top: 168px;
    width: 280px;
    text-align center;
    text-align: center;
    font-family: "DM Serif Display", serif;
    font-size: 62px;
    line-height: 1;
    color: var(--brand-ink);
  }
  .ribbon {
    position: absolute;
    left: 348px;
    top: 250px;
    width: 440px;
    height: 112px;
    background: linear-gradient(90deg, var(--ribbon-dark), var(--ribbon-light) 50%, var(--ribbon-dark));
  }
  .promo-word {
    position: absolute;
    left: 348px;
    top: 288px;
    width: 440px;
    text-align: center;
    font-family: "Playball", cursive;
    font-size: 62px;
    line-height: 1;
    color: var(--promo-ink);
  }
</style>
</head>
<body>
  <main class="can-label">
    <div class="can-label__waves" role="img" aria-label="Layered paper-cut ocean waves in light cyan, royal blue, navy and turquoise"></div>
    <div class="badge"></div>
    <div class="brand-name">Quorvel</div>
    <div class="ribbon" role="img" aria-label="Green satin ribbon banner"></div>
    <div class="promo-word">Promo</div>
  </main>
</body>
</html>
```